Plakat für FBV Erlangen
Zielgruppe
Die FBV Erlangen ist der Kreisverband der Freien Bürgerlichen Vereinigung in Erlangen.
Aufgabenstellung
Es soll ein Plakat (DinA0, Hochformat) designed werden, welches als Basisplakat für verschiedene Veranstaltungen der FBV Erlangen dienen soll. Um dies zu gewährleisten, soll das Plakat eine zentrale freie Fläche mit einer hellen Hintergrundfarbe (z.B. weiß) besitzen, die groß genug ist, um ein ausgedrucktes DinA3 Papier mit Veranstaltungsinformationen darauf zu befestigen.
Das Basisplakat, welches sich an der CI der FBV orientieren soll, soll darüber hinaus das Logo des Kreisverbands Erlangen sowie den Slogan "Bei Ihnen. Direkt. Vor Ort" enthalten. Das FBV-Blau kann bei der Gestaltung des Plakats gerne als Hauptfarbe fungieren.
Ebenfalls enthalten sein soll der Vermerk im Sinne des Pressgesetzes: "VisdP: FBV Erlangen, Amselgrund-Str. 14b, 91047 Erlangen".
Die fertigen Datei soll auch in einem Format vorliegen, das mit Adobe Photoshop oder Illustrator geöffnet und bearbeitet werden kann.
Vielen herzlichen Dank schon mal für Ihre kreativen Entwürfe!

```html
<!DOCTYPE html>
<html lang="de">
<head>
<meta charset="utf-8">
<title>FBV Erlangen – Veranstaltungsplakat</title>
<link href="https://fonts.googleapis.com/css2?family=Fira+Sans:ital,wght@0,700;0,800;1,400;1,800&display=swap" rel="stylesheet">
<style>
  :root {
    --fbv-blue: #0b7ccb;
    --fbv-blue-light: #1fa0e0;
    --sky: #3fb6ea;
    --paper: #ffffff;
    --ink: #111111;
    --frame: #1d8ad4;
  }
  * { margin: 0; padding: 0; box-sizing: border-box; }
  html, body { width: 849px; height: 1200px; overflow: hidden; background: #fff; }
  .poster {
    position: relative;
    width: 849px;
    height: 1200px;
    overflow: hidden;
    font-family: "Fira Sans", sans-serif;
    border: 1.5px solid var(--frame);
    background:
      linear-gradient(172deg, rgba(255,255,255,0) 55%, rgba(180,225,245,0.6) 72%, rgba(63,182,234,0.85) 90%, #2aa9e4 100%),
      linear-gradient(180deg, #f4f9fd 0%, #ffffff 30%, #ffffff 55%, #e3f3fb 75%, #8fd3f2 100%);
  }
  .backdrop-corner {
    position: absolute;
    left: 0; top: 0;
    width: 260px; height: 520px;
    background: linear-gradient(160deg, rgba(60,150,220,0.45) 0%, rgba(140,195,235,0.25) 45%, rgba(255,255,255,0) 85%);
  }
  .backdrop-waves {
    position: absolute;
    left: 0; bottom: 0;
    width: 849px; height: 460px;
    background: linear-gradient(168deg, rgba(255,255,255,0) 20%, rgba(120,205,240,0.35) 55%, rgba(40,170,228,0.55) 100%);
  }
  .brand {
    position: absolute;
    right: 46px; top: 68px;
    display: flex; align-items: center; gap: 14px;
  }
  .brand-mark { width: 34px; height: 34px; background: var(--fbv-blue); }
  .brand-name {
    font-weight: 800;
    font-size: 54px;
    color: var(--fbv-blue);
    letter-spacing: -0.5px;
  }
  .slogan {
    position: absolute;
    font-weight: 800;
    font-style: italic;
    color: var(--fbv-blue);
    line-height: 1;
    letter-spacing: -1px;
    white-space: nowrap;
  }
  .slogan--first { left: 118px; top: 280px; font-size: 88px; }
  .slogan--second { left: 246px; top: 358px; font-size: 128px; letter-spacing: -3px; }
  .slogan--third { left: 382px; top: 488px; font-size: 112px; letter-spacing: -2px; }
  .event-sheet {
    position: absolute;
    left: 72px; top: 509px;
    width: 299px; height: 424px;
    background: var(--paper);
    border: 1px solid #333;
    transform: rotate(-3.6deg);
    box-shadow: 2px 3px 6px rgba(0,0,0,0.25);
    display: flex; align-items: center; justify-content: center;
  }
  .event-sheet__label {
    font-weight: 700;
    font-size: 28px;
    line-height: 1.25;
    text-align: center;
    color: var(--ink);
    letter-spacing: -0.5px;
  }
  .imprint {
    position: absolute;
    right: 46px; bottom: 24px;
    font-style: italic;
    font-weight: 400;
    font-size: 13.5px;
    color: #ffffff;
  }
</style>
</head>
<body>
<div class="poster">
  <div class="backdrop-corner" role="img" aria-label="Weiß-blaues Rautenmuster, weich ausgeblendet"></div>
  <div class="backdrop-waves" role="img" aria-label="Hellblaue, fließende Wellenstruktur im unteren Bereich"></div>

  <div class="brand">
    <span class="brand-mark"></span>
    <span class="brand-name">FBV Erlangen</span>
  </div>

  <div class="slogan slogan--first">Bei Ihnen.</div>
  <div class="slogan slogan--second">Direkt.</div>
  <div class="slogan slogan--third">Vor Ort.</div>

  <div class="event-sheet">
    <p class="event-sheet__label">Veranstaltungs-<br>information</p>
  </div>

  <p class="imprint">VisdP: FBV Erlangen, Amselgrund-Str. 14b, 91047 Erlangen</p>
</div>
</body>
</html>
```